Business card for wedding & event planning company

I'm looking for a well designed double sided business card to represent my wedding and event planning company.

It should include the fact we manage the following events:
Weddings, birthdays, conferences, product launches, fashion shows & conventions
in the following areas:
Wiltshire, Oxfordshire, Berkshire & London

My contact details to be included are:

Moira Pennock
07715 482036
moira@amberlarkcelebrations.co.uk
www.amberlarkcelebrations.co.uk

My logo can be found at the following Filevaultex location:
AI file: https://www.filevaultex.com/s/k4mprt8wn31b7hz/brandlogo_sourcefile.ai?dl=0
PNG file:
https://www.filevaultex.com/s/h9qsle2vbx07mnd/brandlogo_image.png?dl=0

Target Market(s)

women aged 30-55

Industry/Entity Type

Wedding

Contact Information for Business Card

in the following areas:

Moira Pennock
Event Planner
07715 482036

Font styles to use
Serif
Sans Serif
Script

Requirements
Must have
• Purple and white colour scheme
Should not have
• Black background
• Please don't submit any of the see-through business card designs.

```html
<!DOCTYPE html>
<html lang="en">
<head>
<meta charset="utf-8">
<title>Amber Lark Celebrations – Business Card</title>
<link rel="stylesheet" href="https://fonts.googleapis.com/css2?family=Cormorant+Garamond:ital,wght@0,500;1,500&family=Tinos:wght@400;700&display=swap">
<style>
  :root {
    --backdrop: #c9c9cc;
    --purple-deep: #862f8f;
    --purple-mid: #93298f;
    --magenta: #a92a98;
    --magenta-light: #b52b9a;
    --arc-pink: #e8399c;
    --ink-white: #ffffff;
    --ink-soft: #ecd6ec;
    --ghost: rgba(120, 60, 150, 0.35);
  }
  * { margin: 0; padding: 0; box-sizing: border-box; }
  html, body { width: 1200px; height: 1000px; overflow: hidden; }
  body { background: var(--backdrop); position: relative; }

  .card {
    position: absolute;
    width: 643px;
    height: 420px;
    overflow: hidden;
    color: var(--ink-white);
  }
  .card__art { position: absolute; inset: 0; width: 100%; height: 100%; }

  .card--front { left: 102px; top: 95px; z-index: 2; }
  .card--back { left: 455px; top: 485px; z-index: 1; }

  /* Front */
  .brand {
    position: absolute;
    left: 0; right: 0;
    top: 108px;
    text-align: center;
    font-family: "Cormorant Garamond", Georgia, serif;
    font-weight: 500;
    color: var(--ink-white);
  }
  .brand__mark {
    display: block;
    width: 86px; height: 86px;
    margin: 0 auto 10px;
    border: 1.5px solid var(--ink-white);
    border-radius: 50%;
  }
  .brand__name { font-size: 50px; line-height: 1; letter-spacing: 1px; }
  .brand__sub { font-size: 19px; line-height: 1.2; letter-spacing: 3px; margin-top: 2px; }

  .services {
    position: absolute;
    left: 0; right: 0;
    top: 344px;
    text-align: center;
    font-family: "Cormorant Garamond", Georgia, serif;
    font-style: italic;
    font-weight: 500;
    font-size: 21px;
    line-height: 27px;
  }
  .services__dot {
    display: inline-block;
    width: 6px; height: 6px;
    border-radius: 50%;
    background: var(--ink-white);
    vertical-align: middle;
    margin: 0 3px;
  }

  /* Back */
  .contact {
    position: absolute;
    left: 0; width: 646px;
    top: 96px;
    text-align: center;
    font-family: "Tinos", "Times New Roman", serif;
  }
  .contact__name { font-weight: 700; font-size: 26px; line-height: 30px; margin-bottom: 36px; }
  .contact__line { font-size: 24px; line-height: 38px; }

  .areas {
    position: absolute;
    left: 25px;
    top: 320px;
    font-family: "Tinos", "Times New Roman", serif;
    font-size: 19px;
    line-height: 29.5px;
    color: var(--ink-soft);
    list-style: none;
  }
</style>
</head>
<body>

  <section class="card card--front" aria-label="Business card front">
    <svg class="card__art" viewBox="0 0 643 420" aria-hidden="true">
      <defs>
        <linearGradient id="frontBase" x1="0" y1="0" x2="1" y2="1">
          <stop offset="0" stop-color="#86328f"/>
          <stop offset="1" stop-color="#9a2b92"/>
        </linearGradient>
        <linearGradient id="frontDome" x1="0" y1="0" x2="1" y2="1">
          <stop offset="0" stop-color="#8a2a90"/>
          <stop offset="1" stop-color="#a92a97"/>
        </linearGradient>
      </defs>
      <rect width="643" height="420" fill="url(#frontBase)"/>
      <circle cx="330" cy="402" r="362" fill="url(#frontDome)" stroke="var(--arc-pink)" stroke-width="3"/>
    </svg>

    <div class="brand">
      <span class="brand__mark"></span>
      <div class="brand__name">Amber Lark</div>
      <div class="brand__sub">CELEBRATIONS</div>
    </div>

    <p class="services">
      Weddings <span class="services__dot"></span> birthdays <span class="services__dot"></span> conferences <span class="services__dot"></span> product launches<br>
      fashion shows &amp; conventions
    </p>
  </section>

  <section class="card card--back" aria-label="Business card back">
    <svg class="card__art" viewBox="0 0 643 420" aria-hidden="true">
      <defs>
        <linearGradient id="backDome" x1="0" y1="0" x2="1" y2="1">
          <stop offset="0" stop-color="#9a2a93"/>
          <stop offset="1" stop-color="var(--magenta-light)"/>
        </linearGradient>
      </defs>
      <rect width="643" height="420" fill="#87318f"/>
      <circle cx="322" cy="-28" r="392" fill="url(#backDome)" stroke="var(--arc-pink)" stroke-width="3"/>
    </svg>
    <div role="img" aria-label="Faint brand emblem watermark" style="position:absolute;left:165px;top:40px;width:300px;height:300px;border-radius:50%;background:radial-gradient(circle, var(--ghost), rgba(120,60,150,0) 70%);"></div>

    <div class="contact">
      <div class="contact__name">Moira Pennock</div>
      <div class="contact__line">07715 482036</div>
      <div class="contact__line">moira@amberlarkcelebrations.co.uk</div>
      <div class="contact__line">www.amberlarkcelebrations.co.uk</div>
    </div>

    <ul class="areas">
      <li>Wiltshire</li>
      <li>Oxfordshire</li>
      <li>Berkshire &amp; London</li>
    </ul>
  </section>

</body>
</html>
```